Bookcover: Lessons From the Silent Orchard

I am publishing a super-low-cost innovation book for €4,99 on Bravolo Self Release to help everyone become a great innovator: young ambitious people without college education nor a big budget. Do you want to help me?

Brief:
Design a book cover 1600 x 2560 pixels for BSR.
Main title: Lessons From the Silent Orchard
Sub title: mindset - insights - skills & tools
Author: Maarten de Klerk
Design: captive, and appealing to everyone
Target Group: young ambitious people without college education

For bravolo please format the height/width ratio of 1.6:1

```html
<!DOCTYPE html>
<html lang="en">
<head>
<meta charset="utf-8">
<title>Lessons From the Silent Orchard — Book Cover</title>
<link rel="stylesheet" href="https://fonts.googleapis.com/css2?family=Montserrat:wght@700;800;900&display=swap">
<style>
  :root {
    --stage: #f7a43b;
    --paper: #ffffff;
    --cream: #fdf0cc;
    --plum: #8c3f70;
    --plum-deep: #5b2a5f;
    --sun: #f9b800;
    --mauve: #b8679a;
  }
  * { margin: 0; padding: 0; box-sizing: border-box; }
  html, body {
    width: 1200px;
    height: 801px;
    overflow: hidden;
    background: var(--stage);
    font-family: "Montserrat", sans-serif;
  }
  .book-cover {
    position: absolute;
    left: 362px;
    top: 20px;
    width: 476px;
    height: 761px;
    background: var(--paper);
    overflow: hidden;
  }
  .cover-backdrop {
    position: absolute;
    inset: 0;
    width: 100%;
    height: 100%;
  }
  .cover-backdrop path { fill: var(--cream); }
  .author {
    position: absolute;
    left: 46px;
    top: 60px;
    font-weight: 800;
    font-size: 25px;
    letter-spacing: 0.5px;
    color: var(--plum-deep);
    text-transform: uppercase;
    padding-bottom: 6px;
    border-bottom: 2px solid var(--plum-deep);
  }
  .bulb-illustration {
    position: absolute;
    left: 120px;
    top: 130px;
    width: 190px;
    height: 190px;
    border-radius: 50%;
    background: radial-gradient(circle at 45% 45%, var(--sun) 0 55%, rgba(249,184,0,0.25) 56% 100%);
  }
  .title {
    position: absolute;
    left: 0;
    right: 0;
    top: 340px;
    text-align: center;
    font-weight: 900;
    font-size: 58px;
    line-height: 0.98;
    color: var(--plum);
    text-transform: uppercase;
    letter-spacing: 1px;
  }
  .title span { display: block; }
  .subtitle {
    position: absolute;
    left: 0;
    right: 0;
    top: 585px;
    text-align: center;
    font-weight: 800;
    font-size: 14.5px;
    letter-spacing: 0.6px;
    color: var(--plum-deep);
    text-transform: uppercase;
  }
  .plane-illustration {
    position: absolute;
    left: 250px;
    top: 625px;
    width: 150px;
    height: 105px;
    border-radius: 14px;
    background: linear-gradient(160deg, var(--mauve) 0%, rgba(249,184,0,0.35) 100%);
    opacity: 0.8;
  }
</style>
</head>
<body>
  <main class="book-cover">
    <svg class="cover-backdrop" viewBox="0 0 476 761" preserveAspectRatio="none" aria-hidden="true">
      <path d="M0 761 L0 430 C25 345 95 305 175 298 C245 292 258 262 262 205 C268 145 315 118 385 118 C440 118 476 145 476 145 L476 761 Z"/>
    </svg>

    <p class="author">Maarten de Klerk</p>

    <div class="bulb-illustration" role="img" aria-label="Glowing yellow light bulb with rays"></div>

    <h1 class="title">
      <span>Lessons</span>
      <span>From the</span>
      <span>Silent</span>
      <span>Orchard</span>
    </h1>

    <p class="subtitle">Mindset - Insights - Skills &amp; Tools</p>

    <div class="plane-illustration" role="img" aria-label="Paper plane trailing a dashed flight path"></div>
  </main>
</body>
</html>
```